Business card design needed

I need a business card for a new company based in Perth, Western Australia, called KT Power Pty Ltd.

I'm the sole proprietor, and have 25 years' experience in directorship, senior commercial/business development/strategy roles in the oil & gas industry with both supermajors and junior listed companies. I also have interests in renewable energy (and am co-founder and director of a separate renewable energy start-up company). KT Power will be the vehicle for me to contract my services, principally in the oil & gas industry (although this will include directorship services to the renewable energy company). These services will include general consultancy in my areas of expertise, and contracting to provide senior management/director services to start-up or junior oil and gas companies.

I'm looking for a design that communicates professionalism, dynamism, experience, strategic skills and growth.

My ConnectHub profile may also be useful context;

"I have a real passion for discovering new investment opportunities and turning them from talk into reality. Right now my focus is on oil, gas and energy ventures. I’m always on the look out for compelling new investment opportunities where I can bring my leadership and strategic insight to bear to make a real difference by delivering transformational results.

I spent 24 years with HX where I built up extensive international experience in oil, gas and energy and was a member of the company’s “fast track” development programme. As an entrepreneurial senior commercial leader, strategic thinker and tactical dealmaker I was responsible for numerous deals such as divestments, farm-ins, asset swaps, new acreage bids, unitizations, gas and LNG sales, creating billions of dollars of value for HX. These deals frequently broke new ground and/or required an innovative approach that delivered results in excess of what the business thought achievable. I have held senior executive and director roles covering Exploration & Production, Mergers & Acquisitions, Business Development, LNG Marketing, Joint Venture Management, Gas & Power and Corporate head office. International assignments included UK, Australia, Indonesia, Norway & Belgium.

I’m a member of the Guild of Global Fuel Brokers (GGFB) and the Southern Council of Board Members (SCBM).

Board experience comprises four directorships and two alternate directorships of Australian companies, and directorship of a Not for Profit organisation.

Specialties
Strategy, Business Development, Mergers & Acquisitions, Joint Venture Management, Negotiation, Gas & LNG Marketing."

Target Market(s)

Oil and gas or energy companies of all sizes from large listed companies to start-ups - also service providers to the industry.

Industry/Entity Type

Oil And Gas

Contact Information for Business Card

KT Power Pty Ltd
Daniel Hobart
27C Lorne Avenue,
Kelmsdale,
WA 6093

Tel +61 455 823 617
email hobartdk@vellimo.net.au

```html
<!DOCTYPE html>
<html lang="en">
<head>
<meta charset="utf-8">
<title>KT Power – Business Card</title>
<link rel="stylesheet" href="https://fonts.googleapis.com/css2?family=Cinzel:wght@400;600&display=swap">
<style>
  :root {
    --teal: #3ccfcb;
    --teal-deep: #2fb9b8;
    --white: #ffffff;
    --paper: #ffffff;
  }
  html, body {
    margin: 0;
    padding: 0;
    width: 1065px;
    height: 1200px;
    overflow: hidden;
    background: var(--paper);
  }
  .canvas {
    position: relative;
    width: 1065px;
    height: 1200px;
    font-family: "Cinzel", serif;
  }
  .card-back {
    position: absolute;
    left: 408px;
    top: 0;
    width: 637px;
    height: 613px;
    background: var(--teal);
    color: var(--white);
  }
  .holder-name {
    position: absolute;
    left: 103px;
    top: 148px;
    margin: 0;
    font-size: 42px;
    font-weight: 600;
    letter-spacing: 0.5px;
    line-height: 1;
  }
  .contact {
    position: absolute;
    left: 103px;
    top: 244px;
    margin: 0;
    font-style: normal;
    font-size: 30px;
    font-weight: 400;
    line-height: 41.5px;
    letter-spacing: 0.6px;
  }
  .contact .label {
    display: inline-block;
    width: 56px;
  }
  .contact .label-email {
    width: 62px;
  }
  .brand-mark {
    position: absolute;
    display: flex;
    flex-direction: column;
    align-items: center;
    color: var(--teal-deep);
    font-weight: 600;
  }
  .brand-mark .disc {
    border-radius: 50%;
    background: var(--teal);
  }
  .brand-mark--small {
    left: 61px;
    top: 196px;
    width: 300px;
    font-size: 36px;
  }
  .brand-mark--small .disc {
    width: 120px;
    height: 120px;
    margin-bottom: 22px;
  }
  .brand-mark--large {
    left: 305px;
    top: 756px;
    width: 500px;
    font-size: 60px;
  }
  .brand-mark--large .disc {
    width: 210px;
    height: 210px;
    margin-bottom: 34px;
  }
</style>
</head>
<body>
  <main class="canvas">
    <div class="brand-mark brand-mark--small">
      <span class="disc"></span>
      <span class="brand-name">KT Power</span>
    </div>

    <section class="card-back">
      <h1 class="holder-name">Daniel Hobart</h1>
      <address class="contact">
        27C Lorne Avenue,<br>
        Kelmsdale, WA 6093<br>
        Australia<br>
        <span class="label">M.</span>+61 455 823 617<br>
        <span class="label label-email">E.</span>hobartdk@vellimo.net.au
      </address>
    </section>

    <div class="brand-mark brand-mark--large">
      <span class="disc"></span>
      <span class="brand-name">KT Power</span>
    </div>
  </main>
</body>
</html>
```